Interior Design & Furniture E commerce Website Design

I need a cutting edge website design, this is for Interior Design Services as well as eCommerce for furniture and home decor www.lorivelhomestudio.com
Here is a sample of the concept behind the site.
I am a furniture & Interior Designer, want to create a life style brand.
Will offer Interior Design Services : Commercial & Residential (this portion will be a catalog or portfolio type)
The eCommerce side will sell, Furniture, Lighting, Decor, Gifts, Textiles, will also be offering trade so that could be at bottom of site. I also like the concept of concierge as where all the info falls under: shipping, etc..

*Please make sure to make the eCommerce prominent.

Hello Designers, I also would like to possibly update my logo, the current one I like but don't Love.

Target Market(s)

High end customers with disposable income, who also appreciate quality and unique furniture & design

Number of Pages Required

5+ page

Colors
0255a3
f37122

Requirements
Must have
• Room Planer: I will be using this tool http://qtstudio.varnelbex.com/room-planner.inc
• Live Chat
• Will be offering 3d renderings for spaces as well as Virtual Reality
• The image I loaded that looks like copper, I would like to have that as a color on the site with the texture: so the colors are Blue and copper. Would like the site to be user friendly and interactive
• http://qtstudio.varnelbex.com/ (this is the current site in development, so we will be offering Design your own, Trends, inspiration, etc...
• I have included a headshot to use for now about me. or about us.
• I also included several actual project installation (residential and commercial) as well as a variety of my furniture items
• I have Included an old Bio and some articles I would like to show case in a Press Area
• I would also like to include a section for Events (Giving back )I do a lot of charity events 1-2 a year and would like to showcase that as well
• *Please make the store (ecommerce prominent )

```html
<!DOCTYPE html>
<html lang="en">
<head>
<meta charset="utf-8">
<title>Lorivel Home Studio — Interior Design Services</title>
<link href="https://fonts.googleapis.com/css2?family=Montserrat:wght@400;500;600;700&family=Open+Sans:wght@400;600&display=swap" rel="stylesheet">
<style>
:root{
  --orange:#f37122;
  --orange-dark:#d85e14;
  --blue:#0255a3;
  --ink:#333333;
  --muted:#666666;
  --line:#dddddd;
  --paper:#ffffff;
  --mist:#ececec;
  --charcoal:#3d3d3d;
  --night:#262626;
}
*{margin:0;padding:0;box-sizing:border-box}
html,body{width:1200px;height:5341px;overflow:hidden}
body{position:relative;background:var(--paper);font-family:"Open Sans",Arial,sans-serif;color:var(--ink)}
.abs{position:absolute}
.heading{font-family:"Montserrat",Arial,sans-serif;font-weight:600;color:var(--orange);letter-spacing:1px}
.heading .accent{color:var(--blue)}
.section-title{position:absolute;left:0;width:1200px;text-align:center;font-size:38px}
.photo{position:absolute;overflow:hidden}

/* header */
.site-header{position:absolute;left:0;top:0;width:1200px;height:160px;background:var(--paper)}
.brand{position:absolute;left:70px;top:62px;display:flex;align-items:center;gap:12px}
.brand-mark{width:22px;height:22px;border:2px solid var(--orange)}
.brand-name{font-family:"Montserrat",sans-serif;font-weight:600;font-size:26px;color:var(--orange);letter-spacing:3px}
.topline{position:absolute;left:438px;top:40px;font-size:15px;color:var(--muted)}
.search{position:absolute;left:722px;top:34px;width:240px;height:34px;border:1px solid var(--line);border-radius:17px;font-size:14px;color:#aaa;padding:7px 16px}
.search svg{position:absolute;right:12px;top:8px}
.header-rule{position:absolute;left:438px;top:84px;width:530px;height:1px;background:var(--line)}
.nav{position:absolute;left:438px;top:100px;display:flex;gap:34px;font-family:"Montserrat",sans-serif;font-size:15px;font-weight:500;color:var(--ink)}
.nav .current{color:var(--orange)}
.header-divider{position:absolute;left:1010px;top:34px;width:1px;height:90px;background:var(--line)}
.cart{position:absolute;left:1046px;top:50px}
.cart-count{position:absolute;left:1082px;top:46px;width:22px;height:22px;border-radius:50%;background:var(--orange);color:#fff;font-size:12px;text-align:center;line-height:22px}

/* hero */
.hero{position:absolute;left:0;top:160px;width:1200px;height:580px;background:
  linear-gradient(90deg,rgba(25,20,15,.55) 0%,rgba(25,20,15,0) 30%,rgba(25,20,15,0) 70%,rgba(25,20,15,.35) 100%),
  linear-gradient(180deg,#7e8890 0%,#a3aab0 18%,#5f7f86 30%,#6f8b62 42%,#8c7b68 55%,#5a4a3d 75%,#2f2721 100%)}
.hero-title{position:absolute;left:0;top:205px;width:1200px;text-align:center;font-family:"Montserrat",sans-serif;font-weight:600;font-size:86px;color:#fff;letter-spacing:3px}
.hero-sub{position:absolute;left:0;top:322px;width:1200px;text-align:center;font-family:"Montserrat",sans-serif;font-weight:500;font-size:38px;color:#fff}
.slider-arrow{position:absolute;top:274px;width:46px;height:46px;border-radius:50%;background:#fff}

/* about */
.about-title{position:absolute;left:78px;top:865px;font-size:38px}
.about-copy{position:absolute;left:78px;top:925px;width:430px;font-size:15px;line-height:26px;color:var(--muted)}
.about-copy p{margin-bottom:14px}
.btn-outline{position:absolute;left:78px;top:1150px;width:165px;height:50px;border:2px solid var(--orange);font-family:"Montserrat",sans-serif;font-weight:600;font-size:16px;color:var(--ink);text-align:center;line-height:46px}

/* services */
.services-photo{left:0;top:1346px;width:500px;height:434px;background:
  linear-gradient(180deg,rgba(0,0,0,0) 60%,rgba(20,20,20,.55) 100%),
  linear-gradient(100deg,#4d4a48 0%,#8d8884 30%,#b0342c 48%,#c9c2ba 62%,#6a625c 100%)}
.services-panel{position:absolute;left:500px;top:1346px;width:646px;height:434px;background:var(--orange)}
.services-edge{left:1146px;top:1346px;width:54px;height:434px;background:linear-gradient(180deg,#e08a55,#a4532f 50%,#5d3322)}
.services-title{position:absolute;left:70px;top:60px;font-family:"Montserrat",sans-serif;font-weight:600;font-size:36px;color:#fff}
.services-copy{position:absolute;left:70px;top:112px;width:540px;font-size:14px;line-height:22px;color:#fff}
.service-list{position:absolute;left:70px;top:276px;width:560px;display:grid;grid-template-columns:230px 300px;row-gap:16px;list-style:none;font-size:14px;color:#fff}
.service-list li{display:flex;align-items:center;gap:10px}
.service-list li::before{content:"";width:10px;height:10px;border-radius:50%;background:#fff;flex:none}
.service-list .wide{grid-column:1 / 3}

/* featured shop */
.featured{position:absolute;left:0;top:1780px;width:1200px;height:563px;background:var(--mist)}
.product{position:absolute;top:117px;width:235px;height:360px;background:#fff;border:1px solid var(--line);box-shadow:0 2px 6px rgba(0,0,0,.08)}
.product.active{box-shadow:0 6px 18px rgba(0,0,0,.28)}
.product .frame{position:absolute;left:14px;top:14px;width:205px;height:224px;border:1px solid #eee;background:#fff}
.product .shot{position:absolute;left:38px;top:34px;width:129px;height:150px;border-radius:6px}
.product-name{position:absolute;left:0;top:255px;width:100%;text-align:center;font-size:16px;color:var(--muted)}
.add-cart{position:absolute;left:52px;top:300px;width:131px;height:34px;background:#e4e4e4;border:1px solid #d2d2d2;font-size:13px;color:#555;display:flex;align-items:center;justify-content:center;gap:7px}

/* portfolio */
.tabs{position:absolute;left:367px;top:2456px;width:474px;height:36px;display:flex;border:1px solid var(--line)}
.tabs span{flex:1;text-align:center;line-height:34px;font-size:15px;color:var(--muted);border-right:1px solid var(--line)}
.tabs span:last-child{border-right:0}
.tabs .current{color:var(--orange)}

/* testimonial + newsletter */
.testimonial{position:absolute;left:0;top:3222px;width:730px;height:427px;background:var(--charcoal)}
.avatar{position:absolute;left:82px;top:110px;width:100px;height:100px;border-radius:50%;border:4px solid var(--orange);background:linear-gradient(#e8c09c,#b0774f)}
.client{position:absolute;left:210px;top:148px;font-size:15px;color:#ddd}
.quote{position:absolute;left:78px;top:218px;width:635px;font-size:15px;line-height:25px;color:#eee}
.newsletter{position:absolute;left:730px;top:3222px;width:470px;height:427px;background:var(--orange)}
.news-kicker{position:absolute;left:43px;top:138px;font-family:"Montserrat",sans-serif;font-size:24px;color:#fff}
.news-title{position:absolute;left:43px;top:176px;font-family:"Montserrat",sans-serif;font-weight:600;font-size:46px;color:#fff;letter-spacing:1px}
.news-form{position:absolute;left:43px;top:260px;width:295px;height:36px;background:#fff;border-radius:18px;font-size:13px;color:#999;padding:9px 16px}
.news-form .send{position:absolute;right:0;top:0;width:56px;height:36px;border-radius:0 18px 18px 0;background:var(--orange-dark);display:flex;align-items:center;justify-content:center}
.lamps{left:360px;top:0;width:110px;height:300px;background:linear-gradient(180deg,rgba(255,255,255,0) 0%,rgba(255,255,255,.35) 65%,rgba(255,255,255,0) 100%)}

/* press */
.press-item{position:absolute;top:3756px;width:300px;height:367px}
.press-item .cover{position:absolute;left:0;top:0;width:300px;height:367px}
.press-item .caption{position:absolute;left:0;bottom:0;width:300px;height:100px;background:rgba(30,30,30,.8);color:#fff;font-size:15px;line-height:23px;padding:18px 18px}

/* events */
.event{position:absolute;top:4229px;width:333px;height:365px;background:#fff;box-shadow:0 2px 8px rgba(0,0,0,.15)}
.event .shot{position:absolute;left:0;top:0;width:333px;height:205px}
.event-text{position:absolute;left:22px;top:232px;width:180px;font-size:16px;line-height:24px;color:var(--muted)}
.date{position:absolute;left:237px;top:222px;width:72px;height:84px;background:var(--orange);border-radius:36px 36px 0 0;color:#fff;text-align:center;font-family:"Montserrat",sans-serif}
.date .month{display:block;padding-top:14px;font-size:13px;font-weight:600}
.date .day{display:block;font-size:30px;font-weight:600;line-height:34px}

/* contact bar */
.contact-bar{position:absolute;left:0;top:4610px;width:1200px;height:160px;background:var(--orange);color:#fff;font-size:15px;line-height:22px}
.contact-item{position:absolute;top:45px;display:flex;gap:18px;align-items:flex-start}

/* get in touch */
.map{left:0;top:4770px;width:1200px;height:456px;background:linear-gradient(120deg,#e6e3dc 0%,#efece6 40%,#e2e7e0 70%,#e9e5dc 100%)}
.touch-panel{position:absolute;left:160px;top:4780px;width:465px;height:435px;background:#fff;box-shadow:0 2px 8px rgba(0,0,0,.08)}
.touch-title{position:absolute;left:44px;top:30px;font-size:38px}
.field{position:absolute;left:44px;width:350px;border:1px solid #cfcfcf;font-size:14px;color:#999;padding:8px 14px}
.btn-send{position:absolute;left:44px;top:335px;width:135px;height:44px;background:var(--orange);color:#fff;font-family:"Montserrat",sans-serif;font-weight:600;font-size:15px;text-align:center;line-height:44px}
.map-pin{position:absolute;left:800px;top:5025px;display:flex;align-items:center;gap:8px;font-size:14px;color:var(--ink)}

/* footer */
.site-footer{position:absolute;left:0;top:5226px;width:1200px;height:115px;background:var(--night);color:#ddd;text-align:center}
.footer-links{position:absolute;left:0;top:28px;width:1200px;display:flex;justify-content:center;gap:42px;font-size:14px}
.copyright{position:absolute;left:0;top:70px;width:1200px;font-size:14px;color:#bbb}
</style>
</head>
<body>

<header class="site-header">
  <div class="brand"><span class="brand-mark"></span><span class="brand-name">LORIVEL</span></div>
  <div class="topline">Order online or call us 1234567890</div>
  <div class="search">Search...
    <svg width="18" height="18" viewBox="0 0 18 18"><circle cx="7.5" cy="7.5" r="5.5" fill="none" stroke="#555" stroke-width="2"/><line x1="11.5" y1="11.5" x2="16" y2="16" stroke="#555" stroke-width="2"/></svg>
  </div>
  <div class="header-rule"></div>
  <nav class="nav"><span class="current">HOME</span><span>ABOUT</span><span>SERVICES</span><span>SHOP</span><span>BLOG</span><span>CONTACT</span></nav>
  <div class="header-divider"></div>
  <svg class="cart" width="46" height="40" viewBox="0 0 46 40"><path d="M2 6h7l6 22h22l5-16H12" fill="none" stroke="var(--orange)" stroke-width="3" stroke-linejoin="round"/><circle cx="18" cy="34" r="3" fill="var(--orange)"/><circle cx="34" cy="34" r="3" fill="var(--orange)"/></svg>
  <div class="cart-count">0</div>
</header>

<section class="hero" role="img" aria-label="Photo of a luxury lounge with patterned furniture overlooking a pool and ocean view">
  <div class="hero-title">LORI VELHO</div>
  <div class="hero-sub">Interior Design Services</div>
  <div class="slider-arrow" style="left:56px"><svg width="46" height="46" viewBox="0 0 46 46"><path d="M27 14l-9 9 9 9" fill="none" stroke="var(--orange)" stroke-width="3"/></svg></div>
  <div class="slider-arrow" style="left:1098px"><svg width="46" height="46" viewBox="0 0 46 46"><path d="M19 14l9 9-9 9" fill="none" stroke="var(--orange)" stroke-width="3"/></svg></div>
</section>

<section class="about">
  <h2 class="about-title heading">ABOUT <span class="accent">LORI VELHO</span></h2>
  <div class="about-copy">
    <p>As a child, Lori Velho would spend quality time with her Father by helping out in his furniture manufacturing company. She was delighted to be taken along on project installations to exciting places like the Sandcliff Resort in Las Vegas.</p>
    <p>What began as a fun after-school activity evolved into a passion for quality craftsmanship and unique furniture &amp; interior/exterior space design.</p>
  </div>
  <div class="btn-outline">KNOW MORE</div>
  <svg class="abs" style="left:560px;top:800px" width="500" height="440" viewBox="0 0 500 440" role="img" aria-label="Diamond-framed photos of a carved interior, a patterned room and a portrait of the designer">
    <defs>
      <linearGradient id="about-warm" x1="0" y1="0" x2="1" y2="1"><stop offset="0" stop-color="#5e3a26"/><stop offset=".5" stop-color="#b88460"/><stop offset="1" stop-color="#6d4630"/></linearGradient>
      <linearGradient id="about-room" x1="0" y1="0" x2="1" y2="1"><stop offset="0" stop-color="#d8c7b0"/><stop offset=".5" stop-color="#8f6a4e"/><stop offset="1" stop-color="#3e2c22"/></linearGradient>
      <linearGradient id="about-cool" x1="0" y1="0" x2="1" y2="1"><stop offset="0" stop-color="#d9d3ca"/><stop offset=".55" stop-color="#8b6a55"/><stop offset="1" stop-color="#2f7e78"/></linearGradient>
    </defs>
    <polygon points="130,20 240,130 130,240 20,130" fill="url(#about-warm)" stroke="#fff" stroke-width="6"/>
    <polygon points="150,215 245,310 150,405 55,310" fill="url(#about-room)" stroke="#fff" stroke-width="6"/>
    <polygon points="315,20 480,185 315,350 150,185" fill="url(#about-cool)" stroke="#fff" stroke-width="8"/>
  </svg>
</section>

<section class="services">
  <div class="photo services-photo" role="img" aria-label="Photo of a design studio office with red chairs and shelving"></div>
  <div class="services-panel">
    <h2 class="services-title">OUR SERVICES</h2>
    <p class="services-copy">At Lorivel Home Studio, Lori Velho draws on years of hands-on experience in furniture making to shape every interior. Her eye for detail and love of craft guide each room from first sketch to final styling, blending comfort with lasting quality.</p>
    <ul class="service-list">
      <li class="wide">Custom Designed Furniture from concept to production</li>
      <li>Fabric Selections</li><li>Space Planning</li>
      <li>Color Selection</li><li>Accessories and Home Styling</li>
    </ul>
  </div>
  <div class="photo services-edge" role="img" aria-label="Photo detail of a copper toned interior"></div>
</section>

<section class="featured">
  <h2 class="section-title heading" style="top:50px">FEATURED <span class="accent">ITEM</span></h2>
  <svg class="abs" style="left:26px;top:272px" width="20" height="30" viewBox="0 0 20 30"><path d="M16 3L4 15l12 12" fill="none" stroke="var(--orange)" stroke-width="4"/></svg>
  <svg class="abs" style="left:1154px;top:272px" width="20" height="30" viewBox="0 0 20 30"><path d="M4 3l12 12L4 27" fill="none" stroke="var(--orange)" stroke-width="4"/></svg>
  <div class="product" style="left:78px"><div class="frame"><div class="shot" style="background:linear-gradient(160deg,#c9c1b4,#8f8678 60%,#5c5347)" role="img" aria-label="Product photo of an upholstered armchair"></div></div><div class="product-name">Product Name</div><div class="add-cart"><svg width="14" height="12" viewBox="0 0 14 12"><path d="M1 1h2l2 7h7l1-5H4" fill="none" stroke="var(--orange)" stroke-width="1.5"/></svg>Add to Cart</div></div>
  <div class="product" style="left:349px"><div class="frame"><div class="shot" style="background:linear-gradient(160deg,#a87a52,#6e4a2e 60%,#3f2a1a)" role="img" aria-label="Product photo of a carved wooden side table"></div></div><div class="product-name">Product Name</div><div class="add-cart"><svg width="14" height="12" viewBox="0 0 14 12"><path d="M1 1h2l2 7h7l1-5H4" fill="none" stroke="var(--orange)" stroke-width="1.5"/></svg>Add to Cart</div></div>
  <div class="product active" style="left:620px"><div class="frame"><div class="shot" style="background:linear-gradient(160deg,#d6c49a,#a58a55 60%,#5e4a2c)" role="img" aria-label="Product photo of a pair of brass stools"></div></div><div class="product-name">Product Name</div><div class="add-cart"><svg width="14" height="12" viewBox="0 0 14 12"><path d="M1 1h2l2 7h7l1-5H4" fill="none" stroke="var(--orange)" stroke-width="1.5"/></svg>Add to Cart</div></div>
  <div class="product" style="left:883px"><div class="frame"><div class="shot" style="background:linear-gradient(160deg,#6a4d3a,#3d2a1e 60%,#1f150f)" role="img" aria-label="Product photo of a dark wooden dining chair"></div></div><div class="product-name">Product Name</div><div class="add-cart"><svg width="14" height="12" viewBox="0 0 14 12"><path d="M1 1h2l2 7h7l1-5H4" fill="none" stroke="var(--orange)" stroke-width="1.5"/></svg>Add to Cart</div></div>
</section>

<section class="portfolio">
  <h2 class="section-title heading" style="top:2385px">PROJECT <span class="accent">PORTFOLIO</span></h2>
  <div class="tabs"><span class="current">All</span><span>Commercial</span><span>Residential</span></div>
  <div class="photo" style="left:78px;top:2528px;width:331px;height:249px;background:linear-gradient(180deg,#2f3a22 0%,#5e6b36 40%,#8a7a4a 70%,#2a2418 100%)" role="img" aria-label="Project photo of a garden patio lounge"></div>
  <div class="photo" style="left:78px;top:2798px;width:331px;height:342px;background:linear-gradient(180deg,#cfcac0 0%,#a89a86 30%,#7d95a0 50%,#6a5a48 75%,#3e3428 100%)" role="img" aria-label="Project photo of a living room with ocean view"></div>
  <div class="photo" style="left:434px;top:2528px;width:331px;height:338px;background:linear-gradient(180deg,#2a0e0a 0%,#8a2e1e 35%,#c85a3a 55%,#6e2418 80%,#1e0a08 100%)" role="img" aria-label="Project photo of a red-lit restaurant bar"></div>
  <div class="photo" style="left:434px;top:2890px;width:331px;height:250px;background:linear-gradient(180deg,#2e1d12 0%,#7a5234 40%,#b08560 60%,#4a3020 100%)" role="img" aria-label="Project photo of a wood-panelled lounge"></div>
  <div class="photo" style="left:787px;top:2528px;width:334px;height:249px;background:linear-gradient(180deg,#f0ede7 0%,#cfc5b8 40%,#9a8e80 60%,#b8322a 80%,#e8e2da 100%)" role="img" aria-label="Project photo of a bright diner with red stools"></div>
  <div class="photo" style="left:787px;top:2798px;width:334px;height:342px;background:linear-gradient(180deg,#f4f4f4 0%,#dcdcdc 35%,#b2b4b8 60%,#e8e8e8 80%,#8a8c90 100%)" role="img" aria-label="Project photo of a white modern bedroom"></div>
</section>

<section class="testimonial">
  <div class="avatar" role="img" aria-label="Client portrait"></div>
  <div class="client">- Client Name</div>
  <p class="quote">Lorem Ipsum is simply dummy text of the printing and typesetting industry. Lorem Ipsum has been the industry's standard dummy text ever since the 1500s, when an unknown printer took a galley of type and scrambled it to make a type specimen book.</p>
</section>
<section class="newsletter">
  <div class="photo lamps" role="img" aria-label="Photo of hanging pendant lamps"></div>
  <div class="news-kicker">Signup For</div>
  <div class="news-title">NEWSLETTER</div>
  <div class="news-form">Enter Your Email<span class="send"><svg width="20" height="14" viewBox="0 0 20 14"><rect x="1" y="1" width="18" height="12" fill="none" stroke="#fff" stroke-width="1.6"/><path d="M1 1l9 7 9-7" fill="none" stroke="#fff" stroke-width="1.6"/></svg></span></div>
</section>

<section class="press">
  <h2 class="section-title heading" style="top:3688px">PRESS ARTICLES</h2>
  <article class="press-item" style="left:0"><div class="cover" style="background:linear-gradient(180deg,#f4f4f2 0%,#d8d6d2 35%,#8a8680 60%,#4a4642 100%)" role="img" aria-label="Magazine cover featuring the studio"></div><div class="caption">Lorem Ipsum is simply dummy text of printing and typesetting industry.</div></article>
  <article class="press-item" style="left:300px"><div class="cover" style="background:linear-gradient(180deg,#e8e0d4 0%,#a07a58 40%,#6a4a32 70%,#3a2a1e 100%)" role="img" aria-label="Magazine spread with carved furniture"></div><div class="caption">Lorem Ipsum is simply dummy text of printing and typesetting industry.</div></article>
  <article class="press-item" style="left:600px"><div class="cover" style="background:linear-gradient(180deg,#efefed 0%,#c8c2ba 40%,#8a7e72 65%,#4e4640 100%)" role="img" aria-label="Magazine page about interior mosaics"></div><div class="caption">Lorem Ipsum is simply dummy text of printing and typesetting industry.</div></article>
  <article class="press-item" style="left:900px"><div class="cover" style="background:linear-gradient(180deg,#e8e0d4 0%,#a07a58 40%,#6a4a32 70%,#3a2a1e 100%)" role="img" aria-label="Magazine spread with carved furniture"></div><div class="caption">Lorem Ipsum is simply dummy text of printing and typesetting industry.</div></article>
</section>

<section class="events">
  <h2 class="section-title heading" style="top:4165px">LATEST EVENTS</h2>
  <article class="event" style="left:78px"><div class="shot" style="background:linear-gradient(120deg,#dfe6ec 0%,#8fa3b4 40%,#3c5a78 60%,#e0c29a 100%)" role="img" aria-label="Photo of guests at a charity art event"></div><p class="event-text">Lorem Ipsum is simply dummy text of the.</p><div class="date"><span class="month">MAR</span><span class="day">20</span></div></article>
  <article class="event" style="left:434px"><div class="shot" style="background:linear-gradient(120deg,#1c1c20 0%,#4a3a34 40%,#c49a7a 55%,#25252a 100%)" role="img" aria-label="Photo of guests at an evening gala"></div><p class="event-text">Lorem Ipsum is simply dummy text of the.</p><div class="date"><span class="month">MAR</span><span class="day">20</span></div></article>
  <article class="event" style="left:787px"><div class="shot" style="background:linear-gradient(120deg,#e6cfc6 0%,#c9443e 45%,#d98a7a 60%,#7f9a5e 100%)" role="img" aria-label="Photo of hands holding a heart at a giving back event"></div><p class="event-text">Lorem Ipsum is simply dummy text of the.</p><div class="date"><span class="month">MAR</span><span class="day">20</span></div></article>
</section>

<section class="contact-bar">
  <div class="contact-item" style="left:78px">
    <svg width="32" height="42" viewBox="0 0 32 42"><path d="M16 2C8 2 2 8 2 16c0 10 14 24 14 24s14-14 14-24C30 8 24 2 16 2z" fill="#fff"/><circle cx="16" cy="16" r="5" fill="var(--orange)"/></svg>
    <div>Lorivel Home Studio 418 Harlow<br>Ave Brentmoor, CA 90000</div>
  </div>
  <div class="contact-item" style="left:455px">
    <svg width="40" height="40" viewBox="0 0 40 40"><circle cx="20" cy="20" r="19" fill="#fff"/><rect x="10" y="13" width="20" height="14" fill="none" stroke="var(--orange)" stroke-width="2"/><path d="M10 13l10 8 10-8" fill="none" stroke="var(--orange)" stroke-width="2"/></svg>
    <div>Email Us<br>hello@lorivelhomestudio.com</div>
  </div>
  <div class="contact-item" style="left:800px">
    <svg width="40" height="40" viewBox="0 0 40 40"><circle cx="20" cy="20" r="19" fill="#fff"/><path d="M14 11l4 0 2 5-3 2c1 3 3 5 6 6l2-3 5 2v4c0 1-1 2-2 2-10 0-18-8-18-18 0-1 1-2 2-2z" fill="var(--orange)"/></svg>
    <div>Call Us<br>646-555-0142</div>
  </div>
</section>

<section class="touch">
  <div class="photo map" role="img" aria-label="Street map around the studio location"></div>
  <div class="map-pin">
    <svg width="22" height="30" viewBox="0 0 22 30"><path d="M11 1C5 1 1 5 1 11c0 7 10 18 10 18s10-11 10-18C21 5 17 1 11 1z" fill="#d93a2b"/><circle cx="11" cy="11" r="4" fill="#fff"/></svg>
    418 Harlow Avenue
  </div>
  <div class="touch-panel">
    <h2 class="touch-title heading">GET IN TOUCH</h2>
    <div class="field" style="top:86px;height:40px">Name</div>
    <div class="field" style="top:150px;height:40px">Email</div>
    <div class="field" style="top:215px;height:96px">Address</div>
    <div class="btn-send">SEND NOW</div>
  </div>
</section>

<footer class="site-footer">
  <nav class="footer-links"><span>Delivery Information</span><span>Privacy Policy</span><span>Returns</span><span>Sitemap</span><span>Terms &amp; Conditions</span></nav>
  <div class="copyright">©LORIVEL HOME STUDIO , 2018 . All Rights Reserved.</div>
</footer>

</body>
</html>
```